Tallow Creek Advisory Business Card

Hi Morwen. Thank you for your work on my coaching business card. I have another business which needs a new card. It is my counselling business. The best way to find out how to approach this project will be to go to my other website. www.tallowcreekadvisory.com.au and you will be able to see the colours scheme that I will require. White, Green and blue.

The tag line is Tallow Creek Advisory So you can step ahead with ease. The clients are varied but mostly middle class Australian. The card is to show on it the same details as my other business card but with a different phone number. The tag lines are obviously different. The phone number is 9137 2564 The addresses are all the same.

Again simple, professional sophisticated is best.

```html
<!DOCTYPE html>
<html lang="en">
<head>
<meta charset="utf-8">
<title>Tallow Creek Advisory Business Card</title>
<link rel="stylesheet" href="https://fonts.googleapis.com/css2?family=Aldrich&family=Open+Sans:wght@400&display=swap">
<style>
  :root {
    --backdrop: #e6e8eb;
    --card: #ffffff;
    --ink: #2a2a2a;
    --brand-blue: #1f4fa8;
    --brand-green: #3f9a4a;
    --bar-deep: #1a53b8;
    --bar-light: #3a9be0;
    --icon: #ffffff;
  }
  * { margin: 0; padding: 0; box-sizing: border-box; }
  html, body { width: 1200px; height: 816px; overflow: hidden; background: var(--backdrop); }
  .canvas { position: relative; width: 1200px; height: 816px; }
  .card {
    position: absolute; left: 75px; top: 108px; width: 1050px; height: 600px;
    background: var(--card); border-radius: 44px; overflow: hidden;
    box-shadow: 0 10px 30px rgba(0,0,0,0.12);
  }
  .side-bar {
    position: absolute; left: 48px; top: 0; width: 46px; height: 548px;
    border-radius: 0 0 23px 23px;
    background: linear-gradient(180deg, var(--bar-deep) 0%, var(--bar-light) 55%, var(--bar-deep) 100%);
  }
  .bar-icon { position: absolute; left: 56px; width: 30px; height: 30px; }
  .identity { position: absolute; left: 118px; top: 72px; font-family: "Aldrich", sans-serif; color: var(--ink); }
  .identity .person-name { font-size: 30px; line-height: 36px; }
  .identity .person-role { font-size: 28px; line-height: 36px; letter-spacing: 1px; }
  .contact { position: absolute; left: 150px; font-family: "Open Sans", sans-serif; font-size: 24px; line-height: 32px; color: var(--ink); }
  .contact.phone { top: 277px; }
  .contact.online { top: 332px; }
  .contact.address { top: 418px; }
  .brand {
    position: absolute; left: 470px; top: 100px; width: 520px;
  }
  .brand-line {
    display: flex; align-items: center; gap: 14px;
    font-family: "Aldrich", sans-serif; font-size: 34px; line-height: 44px; letter-spacing: 2px;
    color: var(--brand-blue); white-space: nowrap;
  }
  .brand-dot { width: 18px; height: 18px; border-radius: 50%; background: var(--brand-green); flex: none; }
  .brand-rule { height: 3px; width: 488px; margin: 10px 0 10px 32px; background: var(--brand-green); }
  .tagline {
    margin-left: 32px;
    font-family: "Open Sans", sans-serif; font-size: 20px; line-height: 28px;
    color: var(--brand-green); white-space: nowrap;
  }
  .edge-accent {
    position: absolute; right: 0; top: 268px; width: 70px; height: 30px;
    background: linear-gradient(90deg, var(--bar-deep), var(--bar-light));
  }
</style>
</head>
<body>
<div class="canvas">
  <div class="card">
    <div class="side-bar"></div>

    <svg class="bar-icon" style="top:96px" viewBox="0 0 30 30" aria-hidden="true">
      <circle cx="15" cy="10" r="6" fill="var(--icon)"/>
      <path d="M4 27 Q4 17 15 17 Q26 17 26 27 Z" fill="var(--icon)"/>
    </svg>
    <svg class="bar-icon" style="top:278px" viewBox="0 0 30 30" aria-hidden="true">
      <path d="M8 4 L12 4 L14 10 L11 12 Q13 18 18 20 L20 17 L26 19 L26 23 Q24 27 20 26 Q6 22 4 8 Q4 5 8 4 Z" fill="var(--icon)"/>
    </svg>
    <svg class="bar-icon" style="top:330px" viewBox="0 0 30 30" aria-hidden="true">
      <rect x="4" y="8" width="22" height="15" rx="1" fill="var(--icon)"/>
      <path d="M4 8 L15 17 L26 8" fill="none" stroke="var(--bar-light)" stroke-width="2"/>
    </svg>
    <svg class="bar-icon" style="top:366px" viewBox="0 0 30 30" aria-hidden="true">
      <g fill="none" stroke="var(--icon)" stroke-width="2">
        <circle cx="15" cy="15" r="11"/>
        <ellipse cx="15" cy="15" rx="5" ry="11"/>
        <line x1="4" y1="15" x2="26" y2="15"/>
        <line x1="6" y1="9" x2="24" y2="9"/>
        <line x1="6" y1="21" x2="24" y2="21"/>
      </g>
    </svg>
    <svg class="bar-icon" style="top:428px" viewBox="0 0 30 30" aria-hidden="true">
      <path d="M15 4 L28 15 L24 15 L24 26 L18 26 L18 19 L12 19 L12 26 L6 26 L6 15 L2 15 Z" fill="var(--icon)"/>
    </svg>

    <div class="identity">
      <p class="person-name">dana whitlow</p>
      <p class="person-role">GENERAL MANAGER</p>
    </div>

    <p class="contact phone">+61 (03) 9137 2564</p>
    <div class="contact online">
      <p>hello@tallowcreekadvisory.com.au</p>
      <p>www.tallowcreekadvisory.com.au</p>
    </div>
    <div class="contact address">
      <p>418 Wattle Grove Rd,</p>
      <p>Kew East VIC, Australia</p>
    </div>

    <div class="brand">
      <div class="brand-line">
        <span class="brand-dot"></span>
        <span class="brand-name">Tallow Creek Advisory</span>
      </div>
      <div class="brand-rule"></div>
      <p class="tagline">So you can step ahead with ease</p>
    </div>

    <div class="edge-accent"></div>
  </div>
</div>
</body>
</html>
```